Helix Anchor Works Website

Hello we are a screw piling business based in Sydney.
Screw piling is basically drilling steel into the ground with a excavator.

The website needs to have similar information as http://www.brightgroundworks.com.au/. It is basically the same business.

The business name is Helix Anchor Works.

Logo is attached.

Website needs to be wordpress ready.
With SEO.
Want to be able to edit in wordpress.

Target Market(s)

Business to Business and Normal

Industry/Entity Type

Construction

Coding

Coded - Design and coding required

Number of Pages Required

5+ page

Font styles to use
Serif
Sans Serif
Decorative

Requirements
Nice to have
• Information about screw piering.

```html
<!DOCTYPE html>
<html lang="en">
<head>
<meta charset="utf-8">
<title>Helix Anchor Works — Screw Piling Company Based in Sydney</title>
<link href="https://fonts.googleapis.com/css2?family=Raleway:wght@500;600;700&family=Roboto:wght@300;400;500&display=swap" rel="stylesheet">
<style>
:root{
  --blue:#1a6fd1;
  --ink:#222326;
  --text:#3a3b3f;
  --muted:#8a8d93;
  --band:#eceef2;
  --white:#ffffff;
  --panel:#2a2b2e;
  --footer:#141517;
  --bottom:#0c0c0d;
  --rule:#2c2d31;
}
*{margin:0;padding:0;box-sizing:border-box}
html,body{width:756px;height:1200px;overflow:hidden;background:var(--white)}
body{position:relative;font-family:'Roboto',Arial,sans-serif;color:var(--text)}
.abs{position:absolute}
h1,h2,h3,h4{font-family:'Raleway',Arial,sans-serif;font-weight:600}

.site-header{left:0;top:0;width:756px;height:65px;border-bottom:1px solid #e3e4e7}
.brand{left:72px;top:28px;display:flex;align-items:center;gap:7px;font-family:'Raleway',sans-serif;font-weight:700;font-size:15px;color:var(--blue);letter-spacing:.5px}
.brand-mark{width:12px;height:12px;background:var(--blue)}
.quick-call{right:71px;top:36px;font-size:14px;color:var(--ink)}
.quick-call span{color:var(--blue)}

.main-nav{left:0;top:65px;width:756px;height:37px;font-size:7.5px;color:#333}
.main-nav a{position:absolute;top:15px;transform:translateX(-50%);text-decoration:none;color:inherit;white-space:nowrap}
.main-nav a.active{color:var(--blue)}

.hero{left:0;top:102px;width:756px;height:371px;background:linear-gradient(100deg,#5b6a55 0%,#8b7a5c 30%,#5a6d8c 60%,#2b4b7e 100%)}
.hero h1{left:70px;top:186px;font-size:26px;color:var(--white);font-weight:600;letter-spacing:.2px;white-space:nowrap}
.hero p{left:71px;top:223px;width:410px;font-size:7.3px;line-height:16px;color:var(--white)}
.hero-arrows{left:71px;top:281px;display:flex;gap:4px}

.welcome{left:70px;top:410px;width:256px;height:160px;background:var(--panel);padding:22px 20px 0 24px;z-index:2;overflow:hidden}
.welcome h2{font-size:18px;font-weight:500;color:var(--white);line-height:25px;white-space:nowrap}
.welcome h2 span{color:var(--blue)}
.welcome p{margin-top:8px;font-size:7.2px;line-height:16px;color:#9a9ca1;padding-right:4px}
.welcome-photo{left:326px;top:410px;width:360px;height:160px;background:linear-gradient(120deg,#6b6f73,#c9ccce 45%,#8d9196);z-index:2}

.advantages{left:0;top:570px;width:756px;height:199px;background:var(--band)}
.advantages h2{left:68px;top:25px;font-size:16.5px;font-weight:500;color:var(--ink)}
.advantages .lead{left:70px;top:48px;width:320px;font-size:7.2px;line-height:16px;color:var(--muted)}
.advantages ul{left:90px;top:88px;list-style:none;font-size:7.3px;color:#333}
.advantages li{position:relative;height:26px}
.advantages li::before{content:"";position:absolute;left:-1px;top:1px;width:6px;height:6px;border-radius:50%;background:var(--blue)}
.advantages li span{padding-left:9px}
.thumb{width:87px;height:64px;border:2px solid var(--white);box-shadow:0 1px 3px rgba(0,0,0,.25)}

.testimonials{left:0;top:769px;width:756px;height:185px}
.testimonials h2{left:70px;top:27px;font-size:16.5px;font-weight:500;color:var(--ink)}
.avatar{width:68px;height:68px;border-radius:50%;border:2px solid #ddd;background:linear-gradient(#cfd6de,#8d99a8)}
.quote{font-size:7.2px;line-height:13px;color:var(--muted)}
.quote .who{display:block;margin-top:6px;color:var(--blue);font-size:7.5px}
.dots{left:367px;top:151px;display:flex;gap:4px}
.dots i{width:6px;height:6px;border-radius:50%;background:#ccc}
.dots i.on{background:#555}

.partners{left:0;top:954px;width:756px;height:71px;background:var(--band)}
.partners span{position:absolute;top:31px;transform:translateX(-50%);font-family:'Raleway',sans-serif;font-weight:700;font-size:10px;color:#8f9297;letter-spacing:.6px;white-space:nowrap}

.site-footer{left:0;top:1025px;width:756px;height:130px;background:var(--footer);color:#c8c9cc}
.site-footer h3{position:absolute;top:18px;font-size:11.5px;font-weight:500;color:var(--white)}
.site-footer .col{position:absolute;font-size:7px;line-height:16px}
.divider{position:absolute;top:18px;width:1px;height:100px;background:var(--rule)}
.site-footer .sq{display:inline-block;width:7px;height:7px;margin-right:6px;vertical-align:-1px}
.bottom-bar{left:0;top:1155px;width:756px;height:45px;background:var(--bottom);font-size:6.8px;color:#55575c;text-align:center;padding-top:19px}
.bottom-bar a{color:var(--blue);text-decoration:none;margin-left:5px}
</style>
</head>
<body>

<header class="site-header abs">
  <div class="brand abs"><span class="brand-mark"></span>HELIX ANCHOR WORKS</div>
  <div class="quick-call abs"><span>QUICK CALL :</span> 123 456 78900</div>
</header>

<nav class="main-nav abs">
  <a class="active" style="left:156px" href="#">HOME</a>
  <a style="left:235px" href="#">ABOUT US</a>
  <a style="left:323px" href="#">PRODUCTS</a>
  <a style="left:410px" href="#">BENEFITS</a>
  <a style="left:484px" href="#">FAQ</a>
  <a style="left:566px" href="#">NEWS &amp; MEDIA</a>
  <a style="left:662px" href="#">CONTACT US</a>
</nav>

<section class="hero abs" role="img" aria-label="Industrial construction site with steel framework and cleared ground">
  <h1 class="abs">SCREW PILING COMPANY BASED IN SYDNEY</h1>
  <p class="abs">Lorem ipsum dolor sit amet, consectetuer adipiscing elit, sed diam nonummy nibh euismod tincidunt ut laoreet dolore magna aliquam erat volutpat. Ut wisi enim ad minim veniam, quis nostrud exerci tation ullamcorper suscipit lobortis nisl ut aliquip ex ea commodo consequat.</p>
  <div class="hero-arrows abs">
    <svg width="11" height="11" viewBox="0 0 12 12"><circle cx="6" cy="6" r="6" fill="#fff"/><path d="M7 3.5 4.5 6 7 8.5" stroke="#333" stroke-width="1.6" fill="none"/></svg>
    <svg width="11" height="11" viewBox="0 0 12 12"><circle cx="6" cy="6" r="6" fill="#fff"/><path d="M5 3.5 7.5 6 5 8.5" stroke="#333" stroke-width="1.6" fill="none"/></svg>
  </div>
</section>

<section class="welcome abs">
  <h2>WELCOME TO<br><span>HELIX ANCHOR</span> WORKS</h2>
  <p>Ut wisi enim ad minim veniam, quis nostrud exerci tation ullamcorper suscipit lobortis nisl ut aliquip ex ea commodo consequat. Duis autem vel eum iriure dolor in hendrerit in vulputate velit esse molestie consequat.</p>
</section>
<div class="welcome-photo abs" role="img" aria-label="Steel drill bit boring into a metal surface"></div>

<section class="advantages abs">
  <h2 class="abs">ADVANTAGES OF SCREW PILES</h2>
  <p class="lead abs">Ut wisi enim ad minim veniam, quis nostrud exerci tation ullamcorper suscipit lobortis nisl ut aliquip ex ea commodo consequat.</p>
  <ul class="abs">
    <li><span>Nam liber tempor cum soluta nobis eleifend option congue</span></li>
    <li><span>Nihil imperdiet doming id quod mazim placerat facer possim assum</span></li>
    <li><span>Typi non habent claritatem insitam; est usus legentis in iis qui facit eorum claritatem</span></li>
    <li><span>Investigationes demonstraverunt lectores legere me lius quod ii legunt saepius.</span></li>
  </ul>
  <div class="thumb abs" style="left:405px;top:29px;background:linear-gradient(135deg,#3c4654,#b8434a)" role="img" aria-label="Worker measuring steel parts"></div>
  <div class="thumb abs" style="left:501px;top:29px;background:linear-gradient(135deg,#6a4a38,#3a2a22)" role="img" aria-label="Rows of threaded steel rods"></div>
  <div class="thumb abs" style="left:597px;top:29px;background:linear-gradient(135deg,#c7c9c4,#6e7368)" role="img" aria-label="Machinist operating a lathe"></div>
  <div class="thumb abs" style="left:405px;top:107px;background:linear-gradient(135deg,#4a4d50,#b7b9b5)" role="img" aria-label="Milled steel components"></div>
  <div class="thumb abs" style="left:501px;top:107px;background:linear-gradient(135deg,#2d3033,#8b8f93)" role="img" aria-label="Hole saw cutting into metal"></div>
  <div class="thumb abs" style="left:597px;top:107px;background:linear-gradient(135deg,#566274,#9aa3b0)" role="img" aria-label="Pile of drill bits"></div>
</section>

<section class="testimonials abs">
  <h2 class="abs">TESTIMONIALS</h2>
  <div class="avatar abs" style="left:70px;top:67px" role="img" aria-label="Portrait of client Clara Voss"></div>
  <p class="quote abs" style="left:145px;top:80px;width:222px">&ldquo; Lorem ipsum dolor sit amet, consectetuer adipiscing elit, sed diam nonummy nibh euismod tincidunt ut laoreet &rdquo;<span class="who" style="margin-left:-2px">- CLARA VOSS</span></p>
  <div class="avatar abs" style="left:386px;top:67px" role="img" aria-label="Portrait of client Dan Mercer"></div>
  <p class="quote abs" style="left:461px;top:78px;width:222px">&ldquo; Ut wisi enim ad minim veniam, quis nostrud exerci tation ullamcorper suscipit lobortis nisl ut aliquip &rdquo;<span class="who">– DAN MERCER</span></p>
  <div class="dots abs"><i></i><i class="on"></i><i></i></div>
</section>

<section class="partners abs" aria-label="Partner brands">
  <span style="left:109px">SAMPLE LOGO</span>
  <span style="left:200px">BRANDS</span>
  <span style="left:285px">BRAND</span>
  <span style="left:383px">COMPANY</span>
  <span style="left:470px">SAMPLE</span>
  <span style="left:563px">MANUFACTURER</span>
  <span style="left:653px">NORVIK</span>
</section>

<footer class="site-footer abs">
  <h3 style="left:70px">CONTACT US</h3>
  <div class="col" style="left:72px;top:40px;width:135px">
    <div><svg width="6" height="8" viewBox="0 0 6 8" style="margin-right:6px"><path d="M3 0a3 3 0 0 1 3 3c0 2-3 5-3 5S0 5 0 3a3 3 0 0 1 3-3z" fill="#1a6fd1"/></svg>HELIX ANCHOR WORKS</div>
    <div style="padding-left:13px;line-height:12px">361 lorem Ipsm.lorem Ipsm<br>lorem Ipsm lorem 12768</div>
    <div style="margin-top:5px"><svg width="9" height="7" viewBox="0 0 9 7" style="margin-right:5px"><rect width="9" height="7" fill="#1a6fd1"/><path d="M0 0l4.5 4L9 0" stroke="#141517" fill="none"/></svg>info@domainname.com</div>
    <div style="margin-top:6px"><svg width="8" height="8" viewBox="0 0 8 8" style="margin-right:6px"><rect width="8" height="8" rx="2" fill="#1a6fd1"/></svg>123 456 789 000</div>
  </div>
  <div class="divider" style="left:214px"></div>

  <h3 style="left:243px">QUICK LINKS</h3>
  <div class="col" style="left:245px;top:39px">About us<br>Products<br>Benefits<br>FAQ<br>Contact Us</div>
  <div class="divider" style="left:338px"></div>

  <h3 style="left:360px">SOCIAL NETWORKS</h3>
  <div class="col" style="left:362px;top:40px">
    <div><i class="sq" style="background:#3b5b9a"></i>Friendbook</div>
    <div><i class="sq" style="background:#3fa2db"></i>Chirper</div>
    <div><i class="sq" style="background:#2a73b2"></i>Worknet</div>
    <div><i class="sq" style="background:#d4513c"></i>Circlepost</div>
    <div><i class="sq" style="background:#f08a24"></i>RSS</div>
  </div>
  <div class="divider" style="left:484px"></div>

  <h3 style="left:505px">ABOUT US</h3>
  <div class="col" style="left:506px;top:39px;width:180px;line-height:13px">Phasellus dictum nisi nisi, quis cursus ligula ultricies vitae. Aenean mattis magna non lorem venenatis fermentum. Sed ac mauris eget tortor tristique pellentes que. Mauris sed turpis at leo mollis iaculis nec sit amet diam. Duis pharetra arcu nec malesuada rutrum. Mauris dignissim blandit eros,.</div>
</footer>

<div class="bottom-bar abs">Copyright © 2015 Helix Anchor Works. All Rights Reserved. <a href="#">Privacy Policy</a> <a href="#">Terms of Service</a></div>

</body>
</html>
```